Whimsical Aquaculture Farm Packaging Logo

Aquaculture farm in Rhode Island growing hard shell clams (known locally as "quahogs") needs a fun/whimsical (but not silly) label to put on boxes for its "Yuletide Harvest." The "Yuletide Harvest" is actually candy to be given out to friends. The name of the farm is "Perrin Aquaculture Farm."

Boxes are roughly 8x10 so label should fit within those dimensions.

Requirements:
1) Include "Perrin Aquaculture Farm" on the label (it is OK to de-emphasize 'aquaculture' in the type).
2) Include "Yuletide Harvest" (should be more prominent than #1)
3) Do NOT include the year.

Picture of a quahog attached.

Target Market(s)

Existing customers who know us and will get a laugh or chuckle from the playful "Yuletide Harvest" candy.

Industry/Entity Type

Farm

Font styles to use
Serif
Decorative

Colors
33a6d7
85cae6
0892cd
0455a3
3176b5
85acd3

Requirements
Must have
• Should have blue in it (because aquaculture is farming in the ocean).
Should not have
• A date.

```html
<!DOCTYPE html>
<html lang="en">
<head>
<meta charset="utf-8">
<title>Perrin Aquaculture Farm – Yuletide Harvest Labels</title>
<link rel="stylesheet" href="https://fonts.googleapis.com/css2?family=Pinyon+Script&family=Tinos:wght@400;700&display=swap">
<style>
  :root {
    --backdrop: #141414;
    --backdrop-glow: #262626;
    --label-border: #ffffff;
    --sea-light: #33a6d7;
    --sea-mid: #0892cd;
    --sea-deep: #0455a3;
    --sea-band: #3176b5;
    --sea-ink: #1b2f86;
    --photo-light: #8a95a3;
    --photo-dark: #2c3a52;
    --shell-light: #d8c9a6;
    --shell-dark: #8a7656;
    --text-light: #ffffff;
  }
  html, body {
    margin: 0;
    padding: 0;
    overflow: hidden;
  }
  body {
    width: 1200px;
    height: 720px;
    background: radial-gradient(ellipse at center, var(--backdrop-glow) 0%, var(--backdrop) 75%);
    position: relative;
  }
  .label {
    position: absolute;
    display: block;
  }
  .label--landscape { left: 48px; top: 143px; width: 557px; height: 434px; }
  .label--portrait  { left: 718px; top: 81px;  width: 434px; height: 557px; }
  .label__script {
    font-family: "Pinyon Script", cursive;
    fill: var(--text-light);
    stroke: var(--sea-deep);
    stroke-width: 2.5px;
    paint-order: stroke;
  }
  .label__title {
    font-family: "Tinos", "Times New Roman", serif;
    fill: var(--text-light);
    stroke: var(--sea-ink);
    stroke-width: 3px;
    paint-order: stroke;
  }
  .label__farm {
    font-family: "Tinos", "Times New Roman", serif;
    font-weight: 700;
    fill: var(--text-light);
  }
</style>
</head>
<body>

<svg class="label label--landscape" viewBox="0 0 557 434" aria-label="Yuletide Harvest label, landscape">
  <defs>
    <linearGradient id="sea-landscape" x1="0" y1="0" x2="1" y2="1">
      <stop offset="0" stop-color="var(--sea-light)"/>
      <stop offset="1" stop-color="var(--sea-mid)"/>
    </linearGradient>
    <linearGradient id="photo-landscape" x1="0" y1="0" x2="1" y2="1">
      <stop offset="0" stop-color="var(--photo-light)"/>
      <stop offset="0.6" stop-color="var(--photo-dark)"/>
      <stop offset="1" stop-color="var(--sea-deep)"/>
    </linearGradient>
    <radialGradient id="shell-landscape" cx="0.45" cy="0.4" r="0.6">
      <stop offset="0" stop-color="var(--shell-light)"/>
      <stop offset="1" stop-color="var(--shell-dark)"/>
    </radialGradient>
    <radialGradient id="glow-landscape">
      <stop offset="0.55" stop-color="#ffffff" stop-opacity="0.9"/>
      <stop offset="1" stop-color="#ffffff" stop-opacity="0"/>
    </radialGradient>
  </defs>
  <rect class="label__border" width="557" height="434" fill="var(--label-border)"/>
  <rect class="label__sea" x="10" y="9" width="539" height="417" fill="url(#sea-landscape)"/>
  <path class="label__photo" role="img" aria-label="Photo of freshly harvested quahog clams in a blue basket"
        d="M 14 426 C 100 250, 300 60, 549 10 L 549 426 Z" fill="url(#photo-landscape)"/>
  <path class="label__band" d="M 14 426 C 100 250, 300 60, 549 10" fill="none" stroke="var(--sea-band)" stroke-width="12"/>
  <rect x="10" y="9" width="539" height="417" fill="none" stroke="var(--sea-deep)" stroke-width="4"/>
  <ellipse cx="92" cy="168" rx="76" ry="70" fill="url(#glow-landscape)"/>
  <ellipse class="label__shell" role="img" aria-label="Single quahog clam shell"
           cx="92" cy="166" rx="57" ry="52" fill="url(#shell-landscape)"/>
  <text class="label__script" x="147" y="110" font-size="66">Yuletide</text>
  <text class="label__script" x="340" y="200" font-size="62">Harvest</text>
  <text class="label__farm" x="252" y="391" font-size="20">Perrin Aquaculture Farm</text>
  <line x1="246" y1="399" x2="512" y2="399" stroke="var(--text-light)" stroke-width="1.5"/>
</svg>

<svg class="label label--portrait" viewBox="0 0 434 557" aria-label="Yuletide Harvest label, portrait">
  <defs>
    <linearGradient id="sea-portrait" x1="0" y1="0" x2="1" y2="1">
      <stop offset="0" stop-color="var(--sea-mid)"/>
      <stop offset="1" stop-color="var(--sea-light)"/>
    </linearGradient>
    <linearGradient id="photo-portrait" x1="0" y1="0" x2="0.6" y2="1">
      <stop offset="0" stop-color="var(--photo-light)"/>
      <stop offset="0.55" stop-color="var(--photo-dark)"/>
      <stop offset="1" stop-color="var(--sea-deep)"/>
    </linearGradient>
    <radialGradient id="shell-portrait" cx="0.45" cy="0.4" r="0.6">
      <stop offset="0" stop-color="var(--shell-light)"/>
      <stop offset="1" stop-color="var(--shell-dark)"/>
    </radialGradient>
    <radialGradient id="glow-portrait">
      <stop offset="0.55" stop-color="#ffffff" stop-opacity="0.9"/>
      <stop offset="1" stop-color="#ffffff" stop-opacity="0"/>
    </radialGradient>
  </defs>
  <rect class="label__border" width="434" height="557" fill="var(--label-border)"/>
  <rect class="label__sea" x="9" y="9" width="416" height="538" fill="url(#sea-portrait)"/>
  <path class="label__photo" role="img" aria-label="Photo of freshly harvested quahog clams in a blue basket"
        d="M 17 547 C 60 300, 200 90, 425 9 L 425 547 Z" fill="url(#photo-portrait)"/>
  <path class="label__band" d="M 17 547 C 60 300, 200 90, 425 9" fill="none" stroke="var(--sea-band)" stroke-width="12"/>
  <rect x="9" y="9" width="416" height="538" fill="none" stroke="var(--sea-deep)" stroke-width="4"/>
  <text class="label__farm" x="44" y="44" font-size="17">Perrin Aquaculture Farm</text>
  <ellipse cx="95" cy="112" rx="76" ry="68" fill="url(#glow-portrait)"/>
  <ellipse class="label__shell" role="img" aria-label="Single quahog clam shell"
           cx="95" cy="110" rx="58" ry="49" fill="url(#shell-portrait)"/>
  <text class="label__title" x="224" y="268" font-size="60" text-anchor="middle">YULETIDE</text>
  <text class="label__title" x="222" y="360" font-size="54" text-anchor="middle">Harvest</text>
</svg>

</body>
</html>
```